Clipper Chatter, LLC a marketing company needs a logo and business card

I need a logo and business card design. The name of the company is Clipper Chatter, LLC. We hand marketing for vendors in barbershops. I would like for the design of the logo to communicate barbershop conversations that translate to business.

Industry/Entity Type

Marketing

Contact Information for Business Card

Logo needs to be on the business card. Need input fields for Name, Title, Phone, email

Logo Text

Clipper Chatter

Requirements
Must have
• barbershop pole of some sort
Nice to have
• Tagline: Chair talk that works for you

```html
<!DOCTYPE html>
<html lang="en">
<head>
<meta charset="utf-8">
<title>Clipper Chatter, LLC — Business Card</title>
<link rel="stylesheet" href="https://fonts.googleapis.com/css2?family=Lato:wght@400;700&display=swap">
<style>
  :root {
    --navy: #073d7b;
    --red: #e20a17;
    --ink: #111111;
    --paper: #ffffff;
  }
  * { margin: 0; padding: 0; box-sizing: border-box; }
  html, body {
    width: 1200px;
    height: 723px;
    overflow: hidden;
    background: var(--paper);
  }
  .card {
    position: relative;
    width: 1200px;
    height: 723px;
    background: var(--paper);
    font-family: "Lato", sans-serif;
    color: var(--ink);
  }
  .brand-name {
    position: absolute;
    left: 114px;
    top: 230px;
    font-size: 58px;
    font-weight: 700;
    letter-spacing: 1px;
    color: var(--navy);
    text-transform: uppercase;
    line-height: 1;
  }
  .person {
    position: absolute;
    right: 113px;
    top: 322px;
    text-align: right;
  }
  .person-name {
    font-size: 40px;
    font-weight: 700;
    color: var(--navy);
    line-height: 1.1;
  }
  .person-title {
    font-size: 27px;
    font-weight: 400;
    margin-top: 6px;
    line-height: 1.1;
  }
  .divider {
    position: absolute;
    left: 111px;
    top: 420px;
    width: 976px;
    height: 2px;
    background: var(--navy);
  }
  .contact-list {
    position: absolute;
    left: 112px;
    top: 474px;
    list-style: none;
    font-size: 28px;
    line-height: 37px;
  }
  .contact-item {
    display: flex;
    align-items: center;
  }
  .contact-icon {
    width: 24px;
    height: 24px;
    margin-right: 22px;
    fill: var(--navy);
  }
  .address {
    position: absolute;
    right: 113px;
    top: 474px;
    text-align: right;
    font-style: normal;
    font-size: 28px;
    line-height: 37px;
  }
  .footer-band {
    position: absolute;
    left: 0;
    top: 560px;
    width: 1200px;
    height: 163px;
  }
  .tagline {
    position: absolute;
    left: 0;
    top: 618px;
    width: 1200px;
    text-align: center;
    font-size: 29px;
    color: var(--paper);
    text-transform: uppercase;
    line-height: 1;
  }
</style>
</head>
<body>
  <main class="card">
    <div class="brand-name">Clipper Chatter</div>

    <div class="person">
      <div class="person-name">Dana Whitfield</div>
      <div class="person-title">Marketing Specialist</div>
    </div>

    <div class="divider"></div>

    <ul class="contact-list">
      <li class="contact-item">
        <svg class="contact-icon" viewBox="0 0 24 24" aria-hidden="true">
          <path d="M6.6 10.8c1.4 2.8 3.8 5.1 6.6 6.6l2.2-2.2c.3-.3.7-.4 1-.2 1.1.4 2.3.6 3.6.6.6 0 1 .4 1 1V20c0 .6-.4 1-1 1C10.6 21 3 13.4 3 4c0-.6.4-1 1-1h3.5c.6 0 1 .4 1 1 0 1.3.2 2.5.6 3.6.1.3 0 .7-.2 1l-2.3 2.2z"/>
        </svg>
        <span>317 555 0148</span>
      </li>
      <li class="contact-item">
        <svg class="contact-icon" viewBox="0 0 24 24" aria-hidden="true">
          <path d="M2 5h20v14H2z M3.5 6.5 12 13l8.5-6.5" stroke="#fff" stroke-width="1.4" stroke-linejoin="round"/>
        </svg>
        <span>hello@clipperchatter.com</span>
      </li>
    </ul>

    <address class="address">
      2140 N Maple Run Dr<br>
      Greenfield, IN 46140
    </address>

    <svg class="footer-band" viewBox="0 0 1200 163" aria-hidden="true">
      <path d="M8 82 Q600 -50 1192 82 L1192 149 L8 149 Z" fill="var(--red)"/>
      <path d="M8 90 Q600 -30 1192 90 L1192 149 L8 149 Z" fill="var(--navy)"/>
    </svg>
    <p class="tagline">Chair talk that works for you</p>
  </main>
</body>
</html>
```